SaaS Early tech startup business card design

Unique design for experience ecommerce platform company. the business cards will be used by executive members. conformance with color code is required.

```html
<!DOCTYPE html>
<html lang="en">
<head>
<meta charset="utf-8">
<title>Velro Business Card</title>
<link rel="stylesheet" href="https://fonts.googleapis.com/css2?family=Arimo:wght@400;700&display=swap">
<style>
  :root {
    --stage: #2b2b2e;
    --card: #25233d;
    --teal: #1fb9a2;
    --white: #f2f2f6;
    --rule: #c9c9d4;
  }
  * { margin: 0; padding: 0; box-sizing: border-box; }
  html, body {
    width: 1200px; height: 900px; overflow: hidden;
    background: var(--stage);
    font-family: "Arimo", Arial, sans-serif;
  }
  .stage { position: relative; width: 1200px; height: 900px; }
  .card {
    position: absolute; left: 320px;
    width: 560px; height: 320px;
    background: var(--card);
    border-radius: 22px;
    box-shadow: 0 14px 34px rgba(0,0,0,0.45);
    overflow: hidden;
  }
  .card-front { top: 100px; }
  .card-back { top: 480px; }

  .wordmark {
    font-weight: 700; color: var(--teal);
    letter-spacing: -0.02em; line-height: 1;
  }
  .card-front .wordmark {
    position: absolute; left: 0; right: 0; top: 112px;
    text-align: center; font-size: 96px;
  }
  .card-back .wordmark {
    position: absolute; right: 34px; top: 34px; font-size: 72px;
  }

  .holder { position: absolute; left: 34px; top: 40px; }
  .holder-name { font-size: 24px; font-weight: 700; color: var(--teal); letter-spacing: 0.02em; }
  .holder-role { font-size: 16px; color: var(--white); margin-top: 4px; }

  .rule { position: absolute; height: 1px; background: var(--rule); }
  .rule-address { left: 290px; right: 34px; top: 134px; }
  .rule-contact { left: 34px; width: 270px; top: 208px; }

  .address {
    position: absolute; right: 34px; top: 146px;
    text-align: right; font-size: 15px; line-height: 1.35; color: var(--white);
  }

  .contact-list { position: absolute; left: 34px; top: 220px; list-style: none; }
  .contact-item {
    display: flex; align-items: center; gap: 10px;
    font-size: 17px; color: var(--white); height: 28px;
  }
  .contact-icon {
    width: 22px; height: 22px; border-radius: 5px; background: var(--teal);
    display: flex; align-items: center; justify-content: center;
  }
  .contact-icon svg { width: 14px; height: 14px; }
</style>
</head>
<body>
<main class="stage">
  <section class="card card-front" aria-label="Card front">
    <div class="wordmark">velro</div>
  </section>

  <section class="card card-back" aria-label="Card back">
    <div class="holder">
      <div class="holder-name">Daniel Harlow</div>
      <div class="holder-role">Manager</div>
    </div>
    <div class="wordmark">velro</div>
    <div class="rule rule-address"></div>
    <div class="address">48 Harbor Lane, Dunmore<br>Ohio, ZIP 44012</div>
    <div class="rule rule-contact"></div>
    <ul class="contact-list">
      <li class="contact-item">
        <span class="contact-icon">
          <svg viewBox="0 0 24 24"><path fill="#fff" d="M6.6 10.8a15 15 0 0 0 6.6 6.6l2.2-2.2a1 1 0 0 1 1-.25 11.4 11.4 0 0 0 3.6.57 1 1 0 0 1 1 1V20a1 1 0 0 1-1 1A17 17 0 0 1 3 4a1 1 0 0 1 1-1h3.5a1 1 0 0 1 1 1c0 1.25.2 2.45.57 3.57a1 1 0 0 1-.25 1z"/></svg>
        </span>
        555-018-2274
      </li>
      <li class="contact-item">
        <span class="contact-icon">
          <svg viewBox="0 0 24 24"><rect x="3" y="5" width="18" height="14" rx="1.5" fill="none" stroke="#fff" stroke-width="2"/><path d="M3.5 6l8.5 7 8.5-7" fill="none" stroke="#fff" stroke-width="2"/></svg>
        </span>
        hello@velromail.com
      </li>
      <li class="contact-item">
        <span class="contact-icon">
          <svg viewBox="0 0 24 24"><circle cx="12" cy="12" r="9" fill="none" stroke="#fff" stroke-width="2"/><path d="M3 12h18M12 3c3 3 3 15 0 18M12 3c-3 3-3 15 0 18" fill="none" stroke="#fff" stroke-width="1.6"/></svg>
        </span>
        www.velroapp.com
      </li>
    </ul>
  </section>
</main>
</body>
</html>
```